Tervolan Pty Ltd professional business card

A professional business card template using the colours from the supplied logo.
Clean crisp lines while, Modern while not being over the top.

Target Market(s)

Construction, commerical and industrial

Industry/Entity Type

Communications

Contact Information for Business Card

For a Communications, IT, Optical fibre installation company

Colors
37b8a4

```html
<!DOCTYPE html>
<html lang="en">
<head>
<meta charset="utf-8">
<title>Tervolan Pty Ltd – Business Card</title>
<link rel="stylesheet" href="https://fonts.googleapis.com/css2?family=Open+Sans:wght@400;600;700&display=swap">
<style>
  :root {
    --teal: #37b8a4;
    --teal-deep: #2a9c8a;
    --teal-shade: #23806f;
    --night: #1b1020;
    --night-deep: #0e0712;
    --silver-light: #f2f2f2;
    --silver-mid: #b9b9bd;
    --silver-dark: #6d6c72;
    --ink: #1f1f22;
    --paper: #ffffff;
  }
  html, body {
    margin: 0;
    padding: 0;
    width: 863px;
    height: 1200px;
    overflow: hidden;
    background: var(--paper);
  }
  .card-sheet {
    display: block;
    width: 863px;
    height: 1200px;
  }
  .brand-name {
    font-family: "Open Sans", sans-serif;
    font-weight: 700;
    fill: var(--paper);
    letter-spacing: 2px;
  }
  .brand-tagline {
    font-family: "Open Sans", sans-serif;
    font-weight: 400;
  }
  .brand-tagline--dark { fill: var(--ink); }
  .brand-tagline--teal { fill: var(--teal); }
  .contact-text {
    font-family: "Open Sans", sans-serif;
    font-weight: 400;
    font-size: 30px;
    fill: var(--ink);
    letter-spacing: -0.5px;
  }
  .teal { fill: var(--teal); }
  .teal-deep { fill: var(--teal-deep); }
  .icon-tab { fill: #2b2a2e; }
  .icon-glyph { fill: var(--paper); }
</style>
</head>
<body>
<svg class="card-sheet" viewBox="0 0 1062 1476" xmlns="http://www.w3.org/2000/svg" role="img" aria-label="Tervolan Pty Ltd business card, front and back">
  <defs>
    <radialGradient id="night-bg" cx="0.55" cy="0.45" r="0.8">
      <stop offset="0" stop-color="#2a1e2e"/>
      <stop offset="1" stop-color="var(--night-deep)"/>
    </radialGradient>
    <linearGradient id="silver-band" x1="0" y1="0" x2="1" y2="0">
      <stop offset="0" stop-color="var(--silver-dark)"/>
      <stop offset="0.45" stop-color="var(--silver-light)"/>
      <stop offset="1" stop-color="var(--silver-mid)"/>
    </linearGradient>
    <linearGradient id="white-strip" x1="0" y1="0" x2="0" y2="1">
      <stop offset="0" stop-color="#ffffff"/>
      <stop offset="1" stop-color="#dcdcdc"/>
    </linearGradient>
    <linearGradient id="info-panel" x1="0" y1="0" x2="1" y2="1">
      <stop offset="0" stop-color="#ffffff"/>
      <stop offset="0.6" stop-color="#e6e6e6"/>
      <stop offset="1" stop-color="#b8b8bb"/>
    </linearGradient>
  </defs>

  <!-- Front side -->
  <g class="card-front">
    <rect x="0" y="0" width="1062" height="708" fill="url(#night-bg)"/>
    <polygon points="370,0 465,0 615,258 520,258" fill="url(#silver-band)"/>
    <polygon points="480,0 590,0 720,258 610,258" fill="url(#silver-band)"/>
    <polygon points="510,478 610,478 490,708 390,708" fill="url(#silver-band)"/>
    <polygon points="622,478 722,478 592,708 492,708" fill="url(#silver-band)"/>

    <polygon class="teal-deep" points="0,170 445,170 505,258 505,478 450,570 0,570"/>
    <polygon class="teal" points="0,258 880,258 950,368 880,478 0,478"/>
    <polygon points="170,405 902,405 872,462 202,462" fill="url(#white-strip)"/>

    <polygon class="teal" points="1000,122 1062,122 1062,345 1000,345 920,233"/>
    <polygon class="teal" points="1000,393 1062,393 1062,615 1000,615 920,504"/>

    <text class="brand-name" x="884" y="392" text-anchor="end" font-size="82">TERVOLAN</text>
    <text class="brand-tagline brand-tagline--dark" x="858" y="449" text-anchor="end" font-size="44">IT company</text>
  </g>

  <!-- Back side -->
  <g class="card-back">
    <rect x="0" y="767" width="1062" height="709" fill="url(#night-bg)"/>
    <polygon points="180,767 280,767 372,935 272,935" fill="url(#silver-band)"/>
    <polygon points="282,1335 382,1335 300,1476 200,1476" fill="url(#silver-band)"/>

    <polygon class="teal" points="0,935 432,935 555,1135 432,1335 0,1335"/>
    <polygon points="0,970 380,970 472,1135 380,1300 0,1300" fill="url(#info-panel)"/>

    <polygon class="teal" points="1000,890 1062,890 1062,1112 1000,1112 920,1001"/>
    <polygon class="teal" points="1000,1160 1062,1160 1062,1382 1000,1382 920,1271"/>

    <!-- Contact rows -->
    <g class="contact-row">
      <polygon class="icon-tab" points="0,1042 85,1042 104,1071 85,1100 0,1100"/>
      <path class="icon-glyph" d="M55,1056 c3,-3 7,-2 9,1 l4,6 c2,3 1,6 -2,8 l-2,1 c2,5 5,8 10,10 l1,-2 c2,-3 5,-4 8,-2 l6,4 c3,2 4,6 1,9 l-3,3 c-4,4 -14,2 -24,-8 c-10,-10 -12,-20 -8,-24 z"/>
      <text class="contact-text" x="115" y="1082">+61 2 5550 1080</text>
    </g>
    <g class="contact-row">
      <polygon class="icon-tab" points="0,1115 85,1115 104,1144 85,1173 0,1173"/>
      <g fill="none" stroke="#ffffff" stroke-width="3">
        <circle cx="65" cy="1144" r="18"/>
        <ellipse cx="65" cy="1144" rx="8" ry="18"/>
        <line x1="47" y1="1144" x2="83" y2="1144"/>
        <line x1="50" y1="1134" x2="80" y2="1134"/>
        <line x1="50" y1="1154" x2="80" y2="1154"/>
      </g>
      <text class="contact-text" x="113" y="1155">hello@tervolan-it.com</text>
    </g>
    <g class="contact-row">
      <polygon class="icon-tab" points="0,1185 85,1185 104,1214 85,1243 0,1243"/>
      <path class="icon-glyph" d="M65,1196 c-9,0 -16,7 -16,16 c0,11 16,25 16,25 c0,0 16,-14 16,-25 c0,-9 -7,-16 -16,-16 z M65,1206 a6,6 0 1,1 0,12 a6,6 0 1,1 0,-12 z" fill-rule="evenodd"/>
      <text class="contact-text" x="115" y="1223">City . Street . Mall</text>
    </g>

    <text class="brand-name" x="584" y="1165" font-size="70">TERVOLAN</text>
    <text class="brand-tagline brand-tagline--teal" x="583" y="1205" font-size="29">IT company</text>
  </g>
</svg>
</body>
</html>
```